Finance Product Agency Business Card Design

We're an agency that provides products (service contracts, gap insurance, tire and wheel, etc) and support to dealership finance departments. We specialize in training finance producers to maximize their potential and also keep them up to date on the ever changing compliance and legal landscape. I'll attach an image of our logo, excited to see what you all come up with. Would also be interested in discussing our new website design with the winner.

Target Market(s)

auto dealerships

Industry/Entity Type

Business

Contact Information for Business Card

Mark Dolvery
Phone 317.624.5583
Fax 855.472.3308
email Mark.Dolvery@brightlanecoverage.example

Requirements
Must have
• basic contact information
Nice to have
• looking for something professional but modern

```html
<!DOCTYPE html>
<html lang="en">
<head>
<meta charset="utf-8">
<title>Brightlane Coverage Solutions — Business Card</title>
<link rel="stylesheet" href="https://fonts.googleapis.com/css2?family=Open+Sans:wght@400;600;700&display=swap">
<style>
  :root {
    --backdrop: #3a3431;
    --card: #121212;
    --silver: #c9c9c9;
    --text: #e6e6e6;
    --rule: #6e6e6e;
  }
  * { margin: 0; padding: 0; box-sizing: border-box; }
  html, body { width: 1200px; height: 844px; overflow: hidden; }
  body {
    background: var(--backdrop);
    font-family: "Open Sans", Arial, sans-serif;
    position: relative;
  }
  .card {
    position: absolute;
    top: 272px;
    width: 520px;
    height: 300px;
    background: var(--card);
    color: var(--text);
  }
  .card--front { left: 50px; }
  .card--back { left: 630px; }

  .brand {
    display: flex;
    align-items: center;
    gap: 14px;
    position: absolute;
  }
  .brand__dot {
    width: 46px; height: 46px;
    border-radius: 50%;
    background: var(--silver);
    flex: none;
  }
  .brand__name {
    font-weight: 700;
    font-size: 25px;
    line-height: 1.1;
    color: var(--silver);
    letter-spacing: 0.5px;
  }
  .card--front .brand { left: 36px; top: 70px; }
  .card--back .brand { left: 50%; top: 50%; transform: translate(-50%, -50%); }

  .divider {
    position: absolute;
    left: 36px; top: 150px;
    width: 270px; height: 1px;
    background: var(--rule);
  }
  .holder {
    position: absolute;
    right: 24px; top: 138px;
    display: flex; align-items: center; gap: 6px;
    font-weight: 600; font-size: 16px;
  }
  .holder::after {
    content: ""; width: 18px; height: 1px; background: var(--rule);
  }
  .contacts {
    position: absolute;
    right: 42px; top: 172px;
    list-style: none;
    font-size: 13px;
    text-align: right;
    line-height: 22px;
  }
  .contacts li { display: flex; justify-content: flex-end; align-items: center; gap: 8px; }
  .contacts svg { width: 11px; height: 11px; fill: var(--text); }
  .email {
    position: absolute;
    right: 30px; bottom: 44px;
    font-size: 13px;
  }
  .baseline {
    position: absolute;
    left: 36px; right: 24px; bottom: 36px;
    height: 1px; background: var(--rule);
  }
</style>
</head>
<body>
  <section class="card card--front" aria-label="Business card front">
    <div class="brand">
      <span class="brand__dot"></span>
      <span class="brand__name">Brightlane Coverage Solutions</span>
    </div>
    <div class="divider"></div>
    <p class="holder">Mark Dolvery</p>
    <ul class="contacts">
      <li>317.624.5583
        <svg viewBox="0 0 24 24" aria-label="Phone"><path d="M6.6 10.8a15 15 0 0 0 6.6 6.6l2.2-2.2c.3-.3.7-.4 1-.2 1.1.4 2.3.6 3.6.6.6 0 1 .4 1 1V20c0 .6-.4 1-1 1A17 17 0 0 1 3 4c0-.6.4-1 1-1h3.5c.6 0 1 .4 1 1 0 1.3.2 2.5.6 3.6.1.3 0 .7-.2 1z"/></svg>
      </li>
      <li>855.472.3308
        <svg viewBox="0 0 24 24" aria-label="Fax"><path d="M6 2h9l3 3v5H6zM3 11h18v9H3zm3 3v2h5v-2z"/></svg>
      </li>
    </ul>
    <p class="email">Mark.Dolvery@brightlanecoverage.example</p>
    <div class="baseline"></div>
  </section>

  <section class="card card--back" aria-label="Business card back">
    <div class="brand">
      <span class="brand__dot"></span>
      <span class="brand__name">Brightlane Coverage Solutions</span>
    </div>
  </section>
</body>
</html>
```